Lumora business card for a plastic surgeon

we need a business card for plastic surgeons that work on a clinic called LUMORA.
we want a clean design and the following informations: name of the doctor, doctor's registration number (called CRM), telephone, address, facebook, instagram.
Colors: white, blue tones, light brown/ coffee

facebook and instagram: lumoracirurgiaestetica

Industry/Entity Type

Business

Contact Information for Business Card

clean design

Font styles to use
Serif
Sans Serif
Other font styles liked:
• helvetica light

Colors
cee9f5
85cae6
85abd2
3276b5
cfeae6
cedeed
eaf1f7

Requirements
Must have
• doctor's name
• identification number (called CRM)
• contact (phone, facebook, instagram, address)

```html
<!DOCTYPE html>
<html lang="en">
<head>
<meta charset="utf-8">
<title>Lumora business card</title>
<link rel="stylesheet" href="https://fonts.googleapis.com/css2?family=Lato:wght@300;400;700;900&display=swap">
<style>
  :root{
    --backdrop:#2b2b2d;
    --paper:#ffffff;
    --navy:#1d3a6a;
    --navy-deep:#0f1f40;
    --cyan:#22b5d8;
    --coffee:#b58d66;
    --ink-light:#ffffff;
  }
  *{box-sizing:border-box;margin:0;padding:0}
  html,body{width:1200px;height:1000px;overflow:hidden;background:var(--backdrop);font-family:"Lato",Helvetica,Arial,sans-serif}
  .card{position:absolute;left:250px;width:700px;height:400px;background:var(--paper);overflow:hidden;box-shadow:0 10px 30px rgba(0,0,0,.45)}
  .card svg.shapes{position:absolute;inset:0}
  .card--back{top:50px}
  .card--front{top:540px}

  .brand{position:absolute;display:flex;align-items:center;gap:14px;color:var(--cyan);font-weight:400;letter-spacing:4px;white-space:nowrap}
  .brand__dot{width:16px;height:16px;border-radius:50%;background:var(--coffee)}
  .card--back .brand{left:0;right:0;top:150px;justify-content:center;font-size:60px;line-height:1}
  .social{position:absolute;left:0;right:0;top:246px;display:flex;justify-content:center;align-items:center;gap:10px;color:var(--navy);font-size:16px}
  .social__mark{width:24px;height:24px;border-radius:4px;background:var(--navy)}
  .social__mark--alt{background:#6f8aa8}

  .card--front .brand{left:42px;width:328px;top:176px;justify-content:center;font-size:42px;letter-spacing:3px;line-height:1}

  .doctor{position:absolute;left:392px;top:46px;color:var(--ink-light)}
  .doctor__name{font-size:27px;font-weight:300;letter-spacing:.5px;line-height:1.1}
  .doctor__name strong{font-weight:900}
  .doctor__role{font-size:14px;font-weight:700;color:var(--cyan);letter-spacing:1px;line-height:1.2}
  .doctor__crm{font-size:13px;font-weight:700;color:var(--coffee);letter-spacing:1px;line-height:1.3}

  .contact{position:absolute;left:470px;color:var(--ink-light);font-size:16px;line-height:1.25;font-weight:400;white-space:nowrap}
  .contact--phone{top:155px}
  .contact--web{top:225px}
  .contact--address{top:294px;font-size:18px}
</style>
</head>
<body>

<section class="card card--back" aria-label="Card back">
  <svg class="shapes" width="700" height="400" viewBox="0 0 700 400">
    <polygon points="0,0 700,0 700,20 0,70" fill="var(--navy)"/>
    <polygon points="0,70 700,20 700,24 0,74" fill="var(--cyan)"/>
    <polygon points="0,360 700,300 700,400 0,400" fill="var(--navy)"/>
    <polygon points="0,356 700,296 700,300 0,360" fill="var(--cyan)"/>
  </svg>
  <div class="brand"><span class="brand__dot"></span>LUMORA</div>
  <div class="social">
    <span class="social__mark"></span>
    <span class="social__mark social__mark--alt"></span>
    <span>@lumoracirurgiaestetica</span>
  </div>
</section>

<section class="card card--front" aria-label="Card front">
  <svg class="shapes" width="700" height="400" viewBox="0 0 700 400">
    <rect x="0" y="0" width="26" height="400" fill="var(--navy)"/>
    <polygon points="370,0 700,0 700,400 440,400 440,140 370,140" fill="var(--navy)"/>
    <polygon points="370,20 700,20 700,95 370,128" fill="var(--navy-deep)"/>
    <g fill="var(--cyan)">
      <polygon points="364,152 440,152 440,198 376,198"/>
      <polygon points="370,220 440,220 440,266 376,266"/>
      <polygon points="370,288 440,288 440,334 376,334"/>
    </g>
    <g fill="var(--navy)">
      <circle cx="414" cy="175" r="18"/>
      <circle cx="414" cy="243" r="18"/>
      <circle cx="414" cy="311" r="18"/>
    </g>
    <g fill="#fff">
      <path d="M404 172 q10-8 20 0 v3 h-5 v-2 h-10 v2 h-5z"/>
      <rect x="406" y="176" width="16" height="8" rx="1.5"/>
    </g>
    <g fill="none" stroke="#fff" stroke-width="1.6">
      <circle cx="414" cy="243" r="9"/>
      <ellipse cx="414" cy="243" rx="4" ry="9"/>
      <line x1="405" y1="243" x2="423" y2="243"/>
    </g>
    <path d="M414 322 l-6-9 a7 7 0 1 1 12 0z" fill="#fff"/>
    <circle cx="414" cy="308" r="2.5" fill="var(--navy)"/>
  </svg>
  <div class="brand"><span class="brand__dot"></span>LUMORA</div>
  <div class="doctor">
    <p class="doctor__name"><strong>YOUR</strong> NAME</p>
    <p class="doctor__role">DOCTOR</p>
    <p class="doctor__crm">CRM 000000</p>
  </div>
  <p class="contact contact--phone">+000 . 1234 . 5678<br>+000 . 1234 . 5679</p>
  <p class="contact contact--web">lumora@email.com<br>lumora.com</p>
  <p class="contact contact--address">1234 Harbor Lane<br>Brookfield NY 12345</p>
</section>

</body>
</html>
```